Velvet Harbor for sale at the 2019 Tandor Crest Mare Auction on 30 May 2019

I am selling my broodmare at the 2019 Tandor Crest Mare auction on 30 May 2019. I need a flyer to hand out to potential buyers. I have included the required information in the attached word document. I can provide more images if required. I am thinking that a DL double sided or an A5 will suit best. I'm happy to provide more information as required.

Target Market(s)

Race horse breeders, people who buy broodmares.

Font styles to use
Serif
Sans Serif
Script

Colors

Designer to choose colors to be used in the design.

Requirements
Must have
• All of the content provided in the attached brief, however it is not necessary to have the words exactly as per the brief. The brief is for information purposes.
Nice to have
• Innovation...

```html
<!DOCTYPE html>
<html lang="en">
<head>
<meta charset="utf-8">
<title>Velvet Harbor – Broodmare Flyer</title>
<link rel="stylesheet" href="https://fonts.googleapis.com/css2?family=Tinos:wght@400;700&family=Montserrat:wght@700&family=Jost:wght@400&display=swap">
<style>
  :root {
    --stage: #e9e9ea;
    --leather-dark: #2f1a12;
    --leather-mid: #4e2c1d;
    --leather-light: #6a3d28;
    --ink-light: #f4ece4;
    --ink-soft: #e6d9cc;
    --frame: #ffffff;
    --turf: #4f8a2e;
    --turf-light: #7fb24a;
    --sky: #bcd3e6;
  }
  * { box-sizing: border-box; margin: 0; padding: 0; }
  html, body {
    width: 1200px; height: 899px; overflow: hidden;
    background: var(--stage);
  }
  .flyer {
    position: absolute; left: 303px; top: 28px;
    width: 594px; height: 843px;
    background:
      radial-gradient(ellipse at 45% 40%, var(--leather-light) 0%, var(--leather-mid) 45%, var(--leather-dark) 100%);
    color: var(--ink-light);
    text-align: center;
    box-shadow: 0 4px 14px rgba(0,0,0,0.25);
  }
  .flyer__title {
    font-family: "Tinos", serif; font-weight: 400;
    font-size: 40px; letter-spacing: 2px;
    margin-top: 34px; line-height: 1;
  }
  .rule { display: block; margin: 0 auto; }
  .flyer__sale {
    font-family: "Montserrat", sans-serif; font-weight: 700;
    font-size: 15.5px; letter-spacing: 0.6px;
    margin-top: 6px;
  }
  .flyer__lot {
    font-family: "Tinos", serif; font-weight: 700;
    font-size: 14px; margin-top: 8px;
    display: flex; justify-content: center; gap: 14px;
  }
  .flyer__lot .divider { opacity: 0.8; font-weight: 400; }
  .flyer__date {
    font-family: "Tinos", serif; font-weight: 700;
    font-size: 15px; letter-spacing: 0.6px; margin-top: 4px;
  }
  .flyer__pedigree {
    font-family: "Jost", sans-serif; font-size: 12.5px;
    line-height: 1.35; color: var(--ink-soft);
    width: 520px; margin: 10px auto 0;
  }
  .photo {
    background: linear-gradient(180deg, var(--sky) 0%, #8fae7a 28%, var(--turf-light) 45%, var(--turf) 100%);
    border: 5px solid var(--frame);
  }
  .photo--feature {
    width: 530px; height: 250px; margin: 14px auto 0;
  }
  .results {
    display: flex; justify-content: space-between;
    width: 530px; margin: 22px auto 0;
  }
  .result { width: 160px; }
  .photo--small { width: 160px; height: 92px; border-width: 4px; }
  .result__headline {
    font-family: "Tinos", serif; font-weight: 700;
    font-size: 14px; line-height: 1.15; margin-top: 10px;
  }
  .result__detail {
    font-family: "Tinos", serif; font-size: 14px;
    line-height: 1.2; margin-top: 8px; color: var(--ink-soft);
  }
</style>
</head>
<body>
  <main class="flyer">
    <h1 class="flyer__title">VELVET HARBOR</h1>
    <svg class="rule" width="520" height="12" viewBox="0 0 520 12" aria-hidden="true">
      <line x1="8" y1="6" x2="512" y2="6" stroke="#f4ece4" stroke-width="1"/>
      <circle cx="6" cy="6" r="2.5" fill="#f4ece4"/>
      <circle cx="514" cy="6" r="2.5" fill="#f4ece4"/>
    </svg>
    <p class="flyer__sale">2019 TANDOR CREST NATIONAL MARE AUCTION</p>
    <p class="flyer__lot"><span>Lot number: 1414</span><span class="divider">|</span><span>Stable: QC 6</span></p>
    <p class="flyer__date">&#8214; SALE DATE: 30 MAY 2019 &#8214;</p>
    <svg class="rule" width="520" height="12" viewBox="0 0 520 12" aria-hidden="true">
      <line x1="8" y1="6" x2="512" y2="6" stroke="#f4ece4" stroke-width="1"/>
      <circle cx="6" cy="6" r="2.5" fill="#f4ece4"/>
      <circle cx="514" cy="6" r="2.5" fill="#f4ece4"/>
    </svg>
    <p class="flyer__pedigree">In foal to Stone Meadow, sire of: Astral Drive (winner of the Group 3 Coral Bay Stakes by 7.5L), Dust Runner (winner of the Group 2 Kestrel Plate), Harrier Gale (winner of the Tandor Crest Clockwise Classic), Swift Arrow, Copper Nova plus more...</p>

    <div class="photo photo--feature" role="img" aria-label="Photo of Velvet Harbor winning a race at the home straight, field of horses and jockeys on turf"></div>

    <section class="results">
      <article class="result">
        <div class="photo photo--small" role="img" aria-label="Photo of Velvet Harbor crossing the finish line at Hawk Field"></div>
        <h2 class="result__headline">Velvet Harbor beats Pellana by 1.3L</h2>
        <p class="result__detail">Class 6 Plate – 1300m<br>Riverton Racing Club (Hawk Field), 29 April 2017</p>
      </article>
      <article class="result">
        <div class="photo photo--small" role="img" aria-label="Photo of Velvet Harbor winning her debut race"></div>
        <h2 class="result__headline">Velvet Harbor Wins On Debut @The Bayside Coast!</h2>
        <p class="result__detail">Maiden – 1000m<br>Bayside Coast Turf Club, 23 October 2015</p>
      </article>
      <article class="result">
        <div class="photo photo--small" role="img" aria-label="Photo of Velvet Harbor winning by 3.5 lengths"></div>
        <h2 class="result__headline">Velvet Harbor wins by 3.5L</h2>
        <p class="result__detail">Class 6 Handicap – 1400m<br>Riverton Racing Club (Hawk Field), 21 January 2017</p>
      </article>
    </section>
  </main>
</body>
</html>
```